Business Card Re-Design

Consulting Company: To build a high performance organization, you need great leaders at all levels throughout your organization. The Cedar Path Talent Institute engages, inspires, and educates current and future leaders to step beyond the ordinary and deliver exceptional results. This new breed of leaders will motivate your staff to leave the safety of complacency behind and come together to build an extraordinary organization. The current trend has been to ask our people to do more with fewer resources. People have been stepping up to the challenge, but more is required to ensure success with a new work paradigm. We work with your management team to build a successful strategy that will make your organization more effective. CPTI then supports your management team by providing a comprehensive set of proven services to empower your entire organization to successfully execute new strategies.Let CPTI help you optimize your organization’s individual and team performance today!

Target Market(s)

Federal, State and Local Government / Non profit

Industry/Entity Type

Management Consulting

Contact Information for Business Card

CPTI, inc (Cedar Path Talent Institute) Optimizing Individual and Organizational Performance

Colors
fee18a
ec1f27
474747
fbf289

Requirements
Must have
• Professional and high quality feel

```html
<!DOCTYPE html>
<html lang="en">
<head>
<meta charset="utf-8">
<title>Cedar Path Talent Institute – Business Card</title>
<link rel="stylesheet" href="https://fonts.googleapis.com/css2?family=Exo+2:wght@600;700&family=Open+Sans:wght@400&display=swap">
<style>
  :root {
    --backdrop: #e8e5e0;
    --card: #434343;
    --gold: #fee18a;
    --white: #ffffff;
    --text-soft: #e6e6e6;
  }
  html, body {
    margin: 0;
    width: 1200px;
    height: 913px;
    overflow: hidden;
    background: var(--backdrop);
  }
  .canvas {
    position: relative;
    width: 1200px;
    height: 913px;
  }
  .card {
    position: absolute;
    left: 400px;
    top: 106px;
    width: 400px;
    height: 700px;
    background: var(--card);
    box-shadow: 0 14px 40px rgba(0,0,0,0.25);
    overflow: hidden;
  }
  .brand {
    position: absolute;
    left: 0;
    right: 0;
    top: 150px;
    display: flex;
    flex-direction: column;
    align-items: center;
  }
  .brand-row {
    display: flex;
    align-items: center;
    gap: 14px;
  }
  .brand-square {
    width: 54px;
    height: 54px;
    background: var(--gold);
  }
  .brand-name {
    font-family: "Exo 2", sans-serif;
    font-weight: 700;
    font-size: 64px;
    line-height: 1;
    color: var(--white);
    letter-spacing: 1px;
  }
  .brand-full {
    margin-top: 14px;
    font-family: "Exo 2", sans-serif;
    font-weight: 700;
    font-size: 17px;
    color: var(--white);
    letter-spacing: 0.5px;
  }
  .contact {
    position: absolute;
    left: 112px;
    top: 388px;
    font-family: "Open Sans", sans-serif;
    color: var(--text-soft);
  }
  .person-name {
    margin: 0;
    font-family: "Exo 2", sans-serif;
    font-weight: 600;
    font-size: 21px;
    letter-spacing: 0.5px;
    color: var(--gold);
    text-transform: uppercase;
  }
  .person-role {
    margin: 2px 0 0;
    font-size: 15px;
  }
  .address {
    margin: 28px 0 0 22px;
    font-style: normal;
    font-size: 15px;
    line-height: 1.4;
  }
  .channels {
    list-style: none;
    margin: 22px 0 0 38px;
    padding: 0;
    font-size: 15px;
    line-height: 1.7;
  }
  .channels li {
    display: flex;
    align-items: center;
    gap: 10px;
  }
  .channels svg {
    width: 13px;
    height: 13px;
    fill: var(--gold);
    flex: none;
  }
  .edge-band {
    position: absolute;
    left: 0;
    right: 0;
    bottom: 0;
    height: 16px;
    display: flex;
  }
  .edge-band .white { flex: 2.6; background: var(--white); }
  .edge-band .gold { flex: 2; background: var(--gold); }
  .edge-band .white-end { flex: 2.2; background: var(--white); }
</style>
</head>
<body>
<div class="canvas">
  <section class="card" aria-label="Business card for Cedar Path Talent Institute">
    <header class="brand">
      <div class="brand-row">
        <span class="brand-square" aria-hidden="true"></span>
        <span class="brand-name">CPTI, inc</span>
      </div>
      <span class="brand-full">Cedar Path Talent Institute</span>
    </header>

    <div class="contact">
      <h1 class="person-name">Marcus T. Ellery</h1>
      <p class="person-role">President / CEO</p>
      <address class="address">4250 Willow Crest Lane<br>Brookfield, MD 20700</address>
      <ul class="channels">
        <li>
          <svg viewBox="0 0 16 16" aria-label="Phone"><path d="M3.6 1.2l2.3 2.8-1.4 1.8c.9 2 2.6 3.7 4.6 4.6l1.8-1.4 2.8 2.3-1.3 2.4C7.1 15 1 8.9 1.2 2.5z"/></svg>
          301.555.0142
        </li>
        <li>
          <svg viewBox="0 0 16 16" aria-label="Fax"><path d="M4 1h8v4H4z M1 6h14v6h-3v3H4v-3H1z M5.5 10v3.5h5V10z"/></svg>
          301.555.0187
        </li>
        <li>
          <svg viewBox="0 0 16 16" aria-label="Email"><path d="M1 3h14v1.2L8 9 1 4.2z M1 5.8l7 4.8 7-4.8V13H1z"/></svg>
          cptlearn@mail.com
        </li>
      </ul>
    </div>

    <div class="edge-band" aria-hidden="true">
      <span class="white"></span>
      <span class="gold"></span>
      <span class="white-end"></span>
    </div>
  </section>
</div>
</body>
</html>
```